Brightwell Essence colloidal silver spray for pets.

We need a label for an 8-oz cobalt blue spray bottle. We are a small company just starting to share the benefits of colloidal silver. Our first offering will be the 8-oz spray bottle for pets. We would also like to update our logo. The finished project should be crisp and incorporate a dog on the label. I have attached the information we would like on the label and our logo, which can be changed to match your vision.
Updates

Hi, I would like to remind you that we are using a cobalt blue bottle with a black sprayer and would like an updated logo. Also, for the business cards, we don't want an animal on them, as we are planning future products for people. thank you

```html
<!DOCTYPE html>
<html lang="en">
<head>
<meta charset="utf-8">
<title>Brightwell Essence – Colloidal Silver Pet Spray</title>
<link rel="stylesheet" href="https://fonts.googleapis.com/css2?family=Catamaran:wght@400;600;700;800;900&family=Oswald:wght@500&display=swap">
<style>
  :root{
    --lime-bg-1:#f7ffdc;
    --lime-bg-2:#d6f3a0;
    --lime-mid:#e8f8c2;
    --label-top:#dfe3f6;
    --label-mid:#a3abdc;
    --label-low:#5f6c9f;
    --title-green:#21a146;
    --navy:#2d2f93;
    --logo-gray:#6b6c70;
    --leaf-green:#4cae3c;
    --dim-blue:#2f6fb3;
    --paper:#d8d8d8;
    --desk:#ece6de;
    --card:#ffffff;
    --ink:#3b3b3b;
    --dog-gold:#c9975a;
    --dog-shadow:#53627f;
    --flag-red:#d62a2a;
  }
  *{box-sizing:border-box;margin:0;padding:0}
  html,body{width:1200px;height:2859px;overflow:hidden}
  body{font-family:"Catamaran",sans-serif;position:relative;background:#fff}

  .section{position:absolute;left:0;width:1200px}
  .section--product{top:0;height:1200px;background:radial-gradient(circle at 50% 45%,var(--lime-bg-1),var(--lime-bg-2))}
  .section--paper{top:1200px;height:765px;background:var(--paper)}
  .section--cards{top:1965px;height:894px;background:var(--desk)}

  /* brand mark: invented name, one colour, one weight, one plain circle */
  .brand{display:flex;align-items:center;gap:.28em;color:var(--logo-gray);font-weight:800;white-space:nowrap}
  .brand__dot{width:.5em;height:.5em;border-radius:50%;background:var(--leaf-green);flex:none}
  .brand__name{display:block;text-transform:uppercase;letter-spacing:.03em;line-height:.92;text-align:center}

  .brand--hero{position:absolute;left:668px;top:150px;font-size:50px}

  /* label */
  .label{position:absolute;width:297px;height:625px;font-size:10px;overflow:hidden;
    background:linear-gradient(180deg,var(--label-top) 0%,var(--label-mid) 42%,var(--label-low) 62%)}
  .label--main{left:216px;top:372px}
  .label--spec{left:709px;top:461px}
  .label__tab{position:absolute;left:50%;top:0;transform:translateX(-50%);width:108px;height:58px;
    background:#fff;clip-path:polygon(0 0,100% 0,100% 72%,50% 100%,0 72%);
    display:flex;justify-content:center;padding-top:9px}
  .label__tab .brand{font-size:12px}
  .label__title{position:absolute;top:64px;width:100%;text-align:center;font-family:"Oswald",sans-serif;
    font-weight:500;color:var(--title-green);font-size:6.2em;line-height:.95;letter-spacing:-.01em}
  .label__badge{position:absolute;top:200px;left:30px;width:237px;height:54px;border-radius:10px;
    background:var(--navy);color:#fff;font-weight:800;font-size:1.9em;line-height:1.1;
    text-align:center;padding-top:6px;letter-spacing:.02em}
  .label__specs{position:absolute;top:265px;width:100%;text-align:center;color:#fff;font-size:1.35em;line-height:1.1;font-weight:600}
  .label__claims{position:absolute;top:310px;width:100%;text-align:center;color:#fff;font-size:1.2em;line-height:1.08;font-weight:700}
  .label__photo{position:absolute;top:372px;left:0;width:100%;height:253px;
    background:radial-gradient(ellipse at 45% 50%,var(--dog-gold) 0%,#a97c48 38%,var(--dog-shadow) 78%)}
  .label__footer{position:absolute;bottom:12px;left:28px;right:18px;display:flex;justify-content:space-between;align-items:center}
  .origin{display:flex;align-items:center;gap:4px;color:var(--flag-red);font-size:.95em;line-height:1;font-weight:600}
  .origin__flag{width:40px;height:20px;background:linear-gradient(90deg,var(--flag-red) 25%,#fff 25% 75%,var(--flag-red) 75%)}
  .volume{color:#fff;font-weight:700;font-size:1.2em}

  .dim{position:absolute}
  .dim--width{left:709px;top:424px;width:297px;height:14px}
  .dim--height{left:667px;top:461px;width:14px;height:625px}
  .dim__text{position:absolute;font-size:28px;line-height:1;color:var(--dim-blue);font-weight:400;white-space:nowrap;background:var(--lime-mid);padding:0 8px}
  .dim--width .dim__text{left:50%;top:-7px;transform:translateX(-50%)}
  .dim--height .dim__text{left:7px;top:50%;transform:translate(-50%,-50%) rotate(-90deg)}

  /* embossed paper logo */
  .brand--paper{position:absolute;left:50%;top:50%;transform:translate(-50%,-50%);font-size:104px;color:#7a7a7a}

  /* business cards */
  .card{position:absolute;width:500px;height:285px;background:var(--card);box-shadow:0 8px 22px rgba(0,0,0,.18)}
  .card--front{left:560px;top:175px}
  .card--back{left:150px;top:470px}
  .card--front .brand{position:absolute;left:50%;top:50%;transform:translate(-50%,-50%);font-size:46px}
  .card--back .brand{position:absolute;left:40px;top:34px;font-size:32px}
  .contact{position:absolute;left:40px;top:130px;color:var(--ink);font-size:15px;line-height:1.2}
  .contact dt{font-size:12px;letter-spacing:.08em;text-transform:uppercase;color:#777}
  .contact dd{margin-bottom:7px}
</style>
</head>
<body>

<section class="section section--product">
  <div class="brand brand--hero"><span class="brand__dot"></span><span class="brand__name">Brightwell<br>Essence</span></div>

  <article class="label label--main">
    <div class="label__tab"><div class="brand"><span class="brand__name">Brightwell<br>Essence</span></div></div>
    <h1 class="label__title">COLLOIDAL<br>SILVER</h1>
    <p class="label__badge">NATURAL FIRST AID<br>FOR PETS</p>
    <p class="label__specs">10 PPM - No Preservaties<br>100% Pure - No Additives</p>
    <p class="label__claims">Anti microbial, Anti Fungal,<br>Anti Bacterial, Anti Viral<br>Treats burns, Bites, Cuts, Abrasions,<br>Hots Spots</p>
    <div class="label__photo" role="img" aria-label="Photo of a smiling golden retriever"></div>
    <div class="label__footer">
      <span class="origin"><span class="origin__flag" role="img" aria-label="Canadian flag"></span>MADE IN<br>CANADA</span>
      <span class="volume">8 oz / 250 ml</span>
    </div>
  </article>

  <div class="dim dim--width">
    <svg width="297" height="14" viewBox="0 0 297 14"><g stroke="#2f6fb3" stroke-width="1.5" fill="#2f6fb3"><line x1="1" y1="0" x2="1" y2="14"/><line x1="296" y1="0" x2="296" y2="14"/><line x1="2" y1="7" x2="295" y2="7"/><path d="M2 7l10-4v8z"/><path d="M295 7l-10-4v8z"/></g></svg>
    <span class="dim__text">6.20 cm</span>
  </div>
  <div class="dim dim--height">
    <svg width="14" height="625" viewBox="0 0 14 625"><g stroke="#2f6fb3" stroke-width="1.5" fill="#2f6fb3"><line x1="0" y1="1" x2="14" y2="1"/><line x1="0" y1="624" x2="14" y2="624"/><line x1="7" y1="2" x2="7" y2="623"/><path d="M7 2l-4 10h8z"/><path d="M7 623l-4-10h8z"/></g></svg>
    <span class="dim__text">13.00 cm</span>
  </div>

  <article class="label label--spec">
    <div class="label__tab"><div class="brand"><span class="brand__name">Brightwell<br>Essence</span></div></div>
    <h2 class="label__title">COLLOIDAL<br>SILVER</h2>
    <p class="label__badge">NATURAL FIRST AID<br>FOR PETS</p>
    <p class="label__specs">10 PPM - No Preservaties<br>100% Pure - No Additives</p>
    <p class="label__claims">Anti microbial, Anti Fungal,<br>Anti Bacterial, Anti Viral<br>Treats burns, Bites, Cuts, Abrasions,<br>Hots Spots</p>
    <div class="label__photo" role="img" aria-label="Photo of a smiling golden retriever"></div>
    <div class="label__footer">
      <span class="origin"><span class="origin__flag" role="img" aria-label="Canadian flag"></span>MADE IN<br>CANADA</span>
      <span class="volume">8 oz / 250 ml</span>
    </div>
  </article>
</section>

<section class="section section--paper">
  <div class="brand brand--paper"><span class="brand__dot"></span><span class="brand__name">Brightwell<br>Essence</span></div>
</section>

<section class="section section--cards">
  <div class="card card--front">
    <div class="brand"><span class="brand__dot"></span><span class="brand__name">Brightwell<br>Essence</span></div>
  </div>
  <div class="card card--back">
    <div class="brand"><span class="brand__dot"></span><span class="brand__name">Brightwell<br>Essence</span></div>
    <dl class="contact">
      <dt>Web site</dt><dd>www.brightwell-essence.example</dd>
      <dt>Email address</dt><dd>hello@brightwell-essence.example</dd>
      <dt>Telephone</dt><dd>+00 555-0100-000</dd>
    </dl>
  </div>
</section>

</body>
</html>
```